business card for a drum shop (musical intsruments)
north ridge beats
Use same font as used in my logo
marcus hollen
4127 Garvey Oakes Ct
Lower Fenwick, Md 20691
marcus.hollen517@quellmail.net
northridgebeats.com
yes, drum image in middle with url at botton
we will upload ai file shortly. please use this for now.

```html
<!DOCTYPE html>
<html lang="en">
<head>
<meta charset="utf-8">
<title>North Ridge Beats – Business Card</title>
<link rel="stylesheet" href="https://fonts.googleapis.com/css2?family=Josefin+Sans:wght@300&family=Open+Sans:wght@400;700&display=swap">
<style>
  :root {
    --backdrop: #8c8c8c;
    --card: #ffffff;
    --ink: #1e1e1e;
    --ink-soft: #3a3a3a;
    --mark: #2a2a2a;
  }
  * { box-sizing: border-box; margin: 0; padding: 0; }
  html, body {
    width: 1200px;
    height: 908px;
    overflow: hidden;
  }
  body {
    background: var(--backdrop);
    display: flex;
    align-items: center;
    justify-content: center;
    gap: 40px;
    font-family: "Open Sans", Arial, sans-serif;
    color: var(--ink);
  }
  .card {
    position: relative;
    width: 540px;
    height: 309px;
    background: var(--card);
    border-radius: 18px;
    box-shadow: 0 10px 24px rgba(0,0,0,0.25);
    overflow: hidden;
  }

  .brand-dot {
    border-radius: 50%;
    background: var(--mark);
    flex: none;
  }
  .brand-name {
    font-family: "Josefin Sans", "Helvetica Neue", sans-serif;
    font-weight: 300;
    text-transform: uppercase;
    letter-spacing: 0.2em;
    color: var(--mark);
    white-space: nowrap;
  }

  /* Front */
  .card-front .brand-mark {
    position: absolute;
    top: 58px;
    left: 0;
    right: 0;
    display: flex;
    flex-direction: column;
    align-items: center;
    gap: 14px;
  }
  .card-front .brand-dot { width: 116px; height: 116px; }
  .card-front .brand-name {
    font-size: 20px;
    text-align: center;
    padding-left: 0.2em;
  }
  .card-front .website {
    position: absolute;
    bottom: 30px;
    left: 0;
    right: 0;
    text-align: center;
    font-size: 15px;
    font-weight: 700;
    letter-spacing: 0.08em;
  }

  /* Back */
  .card-back .brand-block {
    position: absolute;
    top: 76px;
    left: 40px;
    display: flex;
    align-items: center;
    gap: 14px;
  }
  .card-back .brand-dot { width: 52px; height: 52px; }
  .card-back .brand-name {
    font-size: 20px;
    line-height: 1.3;
  }
  .card-back .brand-name span { display: block; }
  .contact-list {
    position: absolute;
    top: 72px;
    left: 322px;
    list-style: none;
    font-size: 10px;
    color: var(--ink-soft);
    line-height: 1.35;
  }
  .contact-list li {
    display: flex;
    align-items: center;
    gap: 7px;
    margin-bottom: 6px;
    white-space: nowrap;
  }
  .contact-list .address { display: block; margin-bottom: 8px; }
  .contact-icon {
    width: 14px;
    height: 14px;
    flex: none;
  }
  .holder-name {
    position: absolute;
    left: 40px;
    bottom: 46px;
    font-size: 17px;
    font-weight: 700;
    color: var(--ink);
  }
</style>
</head>
<body>

  <section class="card card-front" aria-label="Card front">
    <div class="brand-mark">
      <div class="brand-dot"></div>
      <div class="brand-name">north ridge beats</div>
    </div>
    <div class="website">www.northridgebeats.com</div>
  </section>

  <section class="card card-back" aria-label="Card back">
    <div class="brand-block">
      <div class="brand-dot"></div>
      <div class="brand-name"><span>north ridge</span><span>beats</span></div>
    </div>

    <ul class="contact-list">
      <li class="address">4127 Garvey Oakes Ct<br>Lower Fenwick, Md 20691</li>
      <li>
        <svg class="contact-icon" viewBox="0 0 14 14" aria-hidden="true">
          <circle cx="7" cy="7" r="7" fill="var(--mark)"/>
          <path d="M4.4 3.6l1.5-.2.7 1.7-.9.7c.4.9 1 1.5 1.9 1.9l.7-.9 1.7.7-.2 1.5c-3 .3-6.1-2.8-5.4-5.4z" fill="#fff"/>
        </svg>
        301-555-0148
      </li>
      <li>
        <svg class="contact-icon" viewBox="0 0 14 14" aria-hidden="true">
          <circle cx="7" cy="7" r="7" fill="var(--mark)"/>
          <rect x="3.5" y="4.5" width="7" height="5" fill="none" stroke="#fff" stroke-width="0.9"/>
          <path d="M3.5 4.5L7 7.3l3.5-2.8" fill="none" stroke="#fff" stroke-width="0.9"/>
        </svg>
        marcus.hollen517@quellmail.net
      </li>
      <li>
        <svg class="contact-icon" viewBox="0 0 14 14" aria-hidden="true">
          <circle cx="7" cy="7" r="7" fill="var(--mark)"/>
          <circle cx="7" cy="7" r="3.6" fill="none" stroke="#fff" stroke-width="0.8"/>
          <ellipse cx="7" cy="7" rx="1.6" ry="3.6" fill="none" stroke="#fff" stroke-width="0.8"/>
          <path d="M3.4 7h7.2" stroke="#fff" stroke-width="0.8"/>
        </svg>
        www.northridgebeats.com
      </li>
    </ul>

    <div class="holder-name">Marcus Hollen</div>
  </section>

</body>
</html>
```